edgy fitness flyer

Utilize quote
"I don't want a great body"
by: Nobody Ever
Offer oin back . Vard needs to be edgy and sexy.

Target Market(s)

Women and men 25-45

Industry/Entity Type

Fitness

Requirements
Must have
• clear font layered over gradient image
• See attached sample.
• bright and eye catching
• must coordniate with studio image
• www.plovarfitness.com

```html
<!DOCTYPE html>
<html lang="en">
<head>
<meta charset="utf-8">
<title>Plovar Fitness Rack Cards</title>
<link rel="stylesheet" href="https://fonts.googleapis.com/css2?family=Anton&family=Oswald:wght@400;600;700&family=Arimo:wght@400;700&family=Courier+Prime&display=swap">
<style>
  :root {
    --stage: #1c2426;
    --card-black: #161616;
    --orange: #ef8a26;
    --white: #ffffff;
    --ink: #111111;
  }
  * { margin: 0; padding: 0; box-sizing: border-box; }
  html, body { width: 1200px; height: 1193px; overflow: hidden; background: var(--stage); }
  .stage { position: relative; width: 1200px; height: 1193px; }
  .card { position: absolute; top: 126px; width: 450px; height: 940px; background: var(--card-black); overflow: hidden; }
  .card--front { left: 80px; }
  .card--back { left: 670px; }
  .card-art { position: absolute; inset: 0; }

  .brand-name { position: absolute; left: 0; width: 100%; text-align: center; font-family: "Anton", sans-serif; color: var(--orange); font-size: 58px; line-height: 1; letter-spacing: 1px; white-space: nowrap; }
  .tagline { position: absolute; left: 0; width: 100%; text-align: center; font-family: "Oswald", sans-serif; font-weight: 600; color: var(--white); font-size: 16px; letter-spacing: 1px; white-space: nowrap; }

  .card--front .brand-name { top: 70px; }
  .card--front .tagline { top: 146px; }
  .quote { position: absolute; left: 0; width: 100%; text-align: center; top: 772px; font-family: "Anton", sans-serif; font-size: 40px; color: var(--ink); line-height: 1; white-space: nowrap; }
  .quote-byline { position: absolute; right: 40px; top: 826px; font-family: "Courier Prime", monospace; font-size: 17px; color: var(--ink); white-space: nowrap; }
  .front-url { position: absolute; left: 0; width: 100%; top: 880px; text-align: center; font-family: "Oswald", sans-serif; font-size: 24px; color: var(--ink); }

  .card--back .brand-name { top: 60px; }
  .card--back .tagline { top: 136px; }
  .back-copy { position: absolute; top: 190px; left: 30px; right: 30px; text-align: center; font-family: "Arimo", sans-serif; color: var(--white); font-size: 15px; line-height: 1.32; }
  .back-copy p { margin-bottom: 18px; }
  .back-copy .accent { color: var(--orange); font-weight: 700; font-size: 16.5px; }
  .cta-heading { position: absolute; top: 552px; width: 100%; text-align: center; font-family: "Arimo", sans-serif; font-weight: 700; font-size: 23px; color: var(--white); }
  .class-photo { position: absolute; left: 95px; top: 592px; width: 260px; height: 186px; background: linear-gradient(135deg, #e06a1c 0%, #c9581a 45%, #3a2a22 100%); }
  .join { position: absolute; top: 786px; width: 100%; text-align: center; font-family: "Arimo", sans-serif; font-weight: 700; font-size: 28px; color: var(--white); }
  .locations { position: absolute; top: 826px; left: 60px; right: 30px; display: flex; justify-content: space-between; font-family: "Arimo", sans-serif; color: var(--ink); font-size: 11.5px; line-height: 1.25; }
  .location-name { font-weight: 700; font-size: 14px; }
  .back-url { position: absolute; top: 896px; width: 100%; text-align: center; font-family: "Oswald", sans-serif; font-size: 22px; color: var(--ink); }
</style>
</head>
<body>
<main class="stage">

  <section class="card card--front">
    <svg class="card-art" width="450" height="940" viewBox="0 0 450 940">
      <defs>
        <radialGradient id="couple-tone" cx="55%" cy="50%" r="60%">
          <stop offset="0" stop-color="#c98e6a"/>
          <stop offset="0.55" stop-color="#e6c2a6"/>
          <stop offset="1" stop-color="#ffffff"/>
        </radialGradient>
      </defs>
      <path d="M450 255 C 250 255, 30 420, 30 640 L 30 720 C 170 740, 320 700, 450 640 Z" fill="url(#couple-tone)" role="img" aria-label="Photo of a fit shirtless man and a smiling woman embracing"/>
      <path d="M0 760 C 160 755, 320 700, 450 660 L450 940 L0 940 Z" fill="var(--orange)"/>
    </svg>
    <div class="brand-name">PLOVAR FITNESS</div>
    <div class="tagline">STRONGER EVERY SINGLE SESSION</div>
    <div class="quote">I don’t want a great body</div>
    <div class="quote-byline">by: Nobody Ever</div>
    <div class="front-url">www.plovarfitness.com</div>
  </section>

  <section class="card card--back">
    <svg class="card-art" width="450" height="940" viewBox="0 0 450 940">
      <path d="M0 760 C 120 740, 330 720, 450 690 L450 940 L0 940 Z" fill="var(--orange)"/>
    </svg>
    <div class="brand-name">PLOVAR FITNESS</div>
    <div class="tagline">STRONGER EVERY SINGLE SESSION</div>
    <div class="back-copy">
      <p>”Plovar Fitness stands for Progressive Load Optimized Variable Athletic Routine,” says Dana Reyes, who created the unique exercise program three years ago.</p>
      <p><span class="accent">“We promise 40 minutes, 700 calories,”</span><br>Reyes says, “but clients have been known to burn more than that.” The PLOVAR Fitness routine also promotes Excess Post-Exercise Oxygen Consumption (EPOC).</p>
      <p>PLOVAR Fitness also boasts incredible<br><span class="accent">Yoga classes, Power Ride cycling,</span><br>and soon to come PLOVAR Barre classes.</p>
      <p class="accent">If you are looking get in the best shape of your life, then PLOVAR is the program for you.</p>
    </div>
    <div class="cta-heading">GET DOWN AND SWEATY</div>
    <div class="class-photo" role="img" aria-label="Photo of a group suspension training class in an orange studio"></div>
    <div class="join">Join Us Now</div>
    <div class="locations">
      <div class="location">
        <div class="location-name">Harbor Location</div>
        <div>88 Palmetto Way</div>
        <div>Harbor, FL 30001</div>
        <div>(555) 014-0505</div>
      </div>
      <div class="location">
        <div class="location-name">Lakeview Location</div>
        <div>215 Meridian Avenue</div>
        <div>Lakeview, FL 30000</div>
        <div>(555) 014-2290</div>
      </div>
    </div>
    <div class="back-url">www.plovarfitness.com</div>
  </section>

</main>
</body>
</html>
```